Brochure required for international Sports event

We need an 8 page brochure designed for an international sports event to be hosted in Japan. We are a Travel Company providing packages for participants looking to travel to the event.
The brochure will feature information on the event as well as services our company can provide.
The Brochure is to be an 8 page A4 document in portrait layout.
The brochure needs to be provided both as a print ready document and digital brochure for emailing.
Brochure structure, copy, logo and imagery has been provided
As well as a example brochure design that we like for inspiration.
Link to icons - https://www.filorabox.com/sh/qk3ramvi8ptyzel/BBBqwLpRt7VmK3H9nX2cT8gRb?dl=0
Target Market(s)
Masters/Veterans Sports Participants
Industry/Entity Type
Travel
Colors
Designer to choose colors to be used in the design.
Look and feel

```html
<!DOCTYPE html>
<html lang="en">
<head>
<meta charset="utf-8">
<title>Tour Packages – Package Inclusion</title>
<link rel="stylesheet" href="https://fonts.googleapis.com/css2?family=Didact+Gothic&family=Fredoka:wght@500;600&display=swap">
<style>
  :root {
    --red: #ee0000;
    --purple: #a1068d;
    --lime: #e8fb66;
    --wall: #eeebe6;
    --white: #ffffff;
    --ink: #111111;
  }
  * { margin: 0; padding: 0; box-sizing: border-box; }
  html, body { width: 848px; height: 1200px; overflow: hidden; background: var(--white); }
  .page {
    position: relative; width: 848px; height: 1200px; overflow: hidden;
    background: linear-gradient(180deg, var(--wall) 0%, #f3f1ee 60%, var(--white) 78%);
  }
  .section-tag {
    position: absolute; left: 62px; top: 0; width: 195px; height: 148px;
    background: var(--red); color: var(--white);
    font-family: "Fredoka", sans-serif; font-weight: 500; font-size: 24px; line-height: 31px;
    display: flex; align-items: center; justify-content: center; text-align: center;
  }
  .page-title {
    position: absolute; left: 322px; top: 36px; width: 540px; height: 109px;
    background: var(--purple); border-radius: 55px 0 0 55px;
    color: var(--white); font-family: "Fredoka", sans-serif; font-weight: 500;
    font-size: 45px; line-height: 109px; padding-left: 80px;
  }
  .inclusions {
    position: absolute; left: 0; top: 192px; width: 848px; text-align: center;
    color: var(--purple); font-family: "Fredoka", sans-serif; font-weight: 600;
    font-size: 35px; line-height: 42px;
  }
  .luggage-photo {
    position: absolute; left: 0; top: 405px; width: 848px; height: 500px;
    background: linear-gradient(180deg, #d9d4cc 0%, #3a4a8a 30%, #5a3f46 55%, #2c2d33 85%, #ffffff 100%);
  }
  .intro {
    position: absolute; left: 32px; top: 934px; width: 778px;
    color: var(--purple); font-family: "Didact Gothic", sans-serif;
    font-size: 26px; line-height: 31px; text-align: justify; letter-spacing: 0.3px;
  }
  .page-number {
    position: absolute; left: 771px; top: 1112px; width: 77px; height: 88px;
    background: var(--lime); color: var(--ink);
    font-family: "Didact Gothic", sans-serif; font-size: 20px;
    display: flex; align-items: center; justify-content: center;
  }
</style>
</head>
<body>
<div class="page">
  <div class="section-tag">Tour<br>Packages</div>
  <h1 class="page-title">Package Inclusion</h1>
  <div class="inclusions">
    Flights | Accommodation | Breakfast daily<br>
    Meet &amp; Greet, with bilingual hosts<br>
    Bilingual Local Guides | Transport<br>
    Bullet Train | Sightseeing
  </div>
  <div class="luggage-photo" role="img" aria-label="Colourful suitcases stacked in blue metal luggage cages"></div>
  <p class="intro">Working with Airline and local Accommodation, Travel and Tour partners we have crafted Tour Packages with quality hotels conveniently located to the various sports venues as well as transport links. As no trip to Japan is complete without a visit to Tokyo we have included Japan’s capital and some of the major sights in the package.</p>
  <div class="page-number">5</div>
</div>
</body>
</html>
```